integrative health clinic-Medical massage, acupuncture, chiropractic

we like our logo, but are open to new ideas. We need a new card design. We have added chiropractic and acupuncture that we have put under the name of the business. We are an integrative medical clinic

Target Market(s)

General public, athletes

Contact Information for Business Card

Phone 5055583927
Fax 5055583926
Hours Monday-Friday 9-6
Saturday 10-6
The 20% can be smaller on the back

Colors
3176b5
0355a3

Requirements
Must have
• Logo but am open to ideas
Nice to have
• We are an integrated medical clinic but also want to be personable. We want the card fun and inviting

```html
<!DOCTYPE html>
<html lang="en">
<head>
<meta charset="utf-8">
<title>Open Path Wellness – Business Cards</title>
<link rel="stylesheet" href="https://fonts.googleapis.com/css2?family=Roboto+Condensed:ital,wght@0,400;0,700;1,400&family=Roboto:wght@400;500;700&display=swap">
<style>
  :root {
    --brand-blue: #3176b5;
    --brand-navy: #0355a3;
    --ink: #1b1b1b;
    --paper: #ffffff;
    --backdrop: #e9ecef;
    --muted: #5a6f86;
  }
  * { box-sizing: border-box; margin: 0; padding: 0; }
  html, body { width: 1200px; height: 818px; overflow: hidden; }
  body {
    background: var(--backdrop);
    font-family: "Roboto", Arial, sans-serif;
    position: relative;
  }
  .card {
    position: absolute;
    top: 259px;
    width: 525px;
    height: 300px;
    background: var(--paper);
    border-radius: 26px;
    overflow: hidden;
    box-shadow: 0 6px 18px rgba(0,0,0,.12);
  }
  .card--front { left: 50px; }
  .card--back { left: 625px; }
  .card__band { position: absolute; left: 0; bottom: 0; width: 100%; height: 100%; }

  /* front */
  .brand {
    position: absolute; left: 34px; top: 40px;
    display: flex; align-items: center; gap: 12px;
  }
  .brand__dot { width: 26px; height: 26px; border-radius: 50%; background: var(--brand-navy); }
  .brand__name {
    font-family: "Roboto Condensed", Arial, sans-serif;
    font-weight: 700; font-size: 40px; color: var(--ink); letter-spacing: -.5px;
  }
  .brand__tagline {
    position: absolute; left: 72px; top: 92px;
    font-family: "Roboto Condensed", Arial, sans-serif;
    font-style: italic; font-size: 17px; color: var(--ink);
  }
  .front__services {
    position: absolute; left: 30px; top: 172px;
    color: #fff; font-size: 11px; letter-spacing: .3px;
  }
  .front__contact {
    position: absolute; left: 30px; top: 196px;
    color: #fff; font-size: 12px;
  }
  .front__hours {
    position: absolute; left: 30px; top: 236px;
    color: #fff; font-size: 15px; font-weight: 500;
  }
  .offer {
    position: absolute; right: 30px; top: 140px; text-align: right;
    color: var(--brand-blue);
  }
  .offer__value { font-size: 50px; font-weight: 500; line-height: 1; }
  .offer__label { font-size: 11px; letter-spacing: 1px; margin-top: 4px; }

  /* back */
  .person {
    position: absolute; left: 30px; top: 26px;
    color: var(--brand-blue); font-size: 20px; font-weight: 700; letter-spacing: 1px;
  }
  .person__details {
    position: absolute; left: 30px; top: 56px;
    font-size: 11.5px; line-height: 1.5; color: var(--muted);
  }
  .back__mark {
    position: absolute; left: 190px; top: 100px;
    width: 54px; height: 54px; border-radius: 50%; background: var(--brand-navy);
  }
  .specialty {
    position: absolute; right: 30px; top: 96px; width: 200px;
    color: var(--brand-blue); font-size: 15px; line-height: 1.35; text-align: right;
  }
  .email {
    position: absolute; left: 60px; top: 200px;
    color: var(--brand-blue); font-size: 14px;
  }
</style>
</head>
<body>

<section class="card card--front" aria-label="Card front">
  <svg class="card__band" viewBox="0 0 525 300" preserveAspectRatio="none" aria-hidden="true">
    <path d="M0 150 H300 Q330 150 335 170 L345 200 Q350 212 360 212 H525 V300 H0 Z" fill="var(--brand-blue)"/>
    <path d="M0 140 H300 Q320 140 326 154" fill="none" stroke="var(--brand-navy)" stroke-width="5"/>
    <rect x="0" y="282" width="525" height="18" fill="var(--brand-navy)"/>
  </svg>
  <div class="brand">
    <span class="brand__dot"></span>
    <span class="brand__name">Open Path Wellness</span>
  </div>
  <p class="brand__tagline">Spinal Therapy and Wellness Center</p>
  <p class="front__services">Medical Massage • Acupuncture • Chiropractic</p>
  <p class="front__contact">Phone 505.557.6140 &nbsp;•&nbsp; Fax 505.557.6139</p>
  <p class="front__hours">Hours: Monday-Friday 9-6 &amp; Saturday 10-6</p>
  <div class="offer">
    <p class="offer__value">20%</p>
    <p class="offer__label">OFF FIRST VISIT</p>
  </div>
</section>

<section class="card card--back" aria-label="Card back">
  <svg class="card__band" viewBox="0 0 525 300" preserveAspectRatio="none" aria-hidden="true">
    <path d="M0 238 H400 Q440 238 460 215 L480 195 Q490 186 525 186 V300 H0 Z" fill="var(--brand-blue)"/>
    <path d="M0 228 H400 Q430 228 448 210" fill="none" stroke="var(--brand-navy)" stroke-width="4"/>
  </svg>
  <h1 class="person">DANIEL REYES</h1>
  <p class="person__details">
    210 Mesa Verde Dr NE, Suite 8<br>
    Albuquerque, NM 87110<br>
    Tel 505.557.6140<br>
    Fax 505.557.6139
  </p>
  <span class="back__mark"></span>
  <p class="specialty">Specializing in Medical Massage, Acupuncture and Chiropractic Care</p>
  <p class="email">hello@openpathwellness.com</p>
</section>

</body>
</html>
```